International gaming entertainment company is looking for an innovative Power Point design *

We are looking for a Power Point design for potential international investors, partners and customers in the gaming industry, meaning that a reference to internationality and gaming should become apparent.
The template should be in a reduced and clear style with a combination of innovation and tradition. It should be adaptive and suitable for various applications (tables, shapes and diagrams).
The color scheme of our company are various shades of gray and burgundy (wine-red), however as for the design in question, we are open to other meaningful suggestions (no garish colors).
Updates

Noch kein Design dabei, dass uns 100%ig überzeugt

Target Market(s)

International investors and partners in the gaming industry

Font styles to use
Serif
Sans Serif
Other font styles liked:
• Interstate

Requirements
Must have
• Clear lines
Modern
Footer line with room for classification (eg Confidential, Public) and page number

```html
<!DOCTYPE html>
<html lang="en">
<head>
<meta charset="utf-8">
<title>Presentation Deck – Meridian Gaming</title>
<link href="https://fonts.googleapis.com/css2?family=Roboto:wght@300;400;700;900&family=Roboto+Condensed:wght@400;700&display=swap" rel="stylesheet">
<style>
:root{
  --red:#e3051b;
  --red-dark:#b00315;
  --ink:#222;
  --gray:#777;
  --gray-light:#d9d9d9;
  --gray-bg:#efefef;
  --white:#fff;
}
*{box-sizing:border-box;margin:0;padding:0}
html,body{width:1200px;height:2336px;overflow:hidden;background:var(--white);font-family:"Roboto",sans-serif;color:var(--ink)}
.canvas{position:relative;width:1200px;height:2336px;overflow:hidden}

/* hero */
.hero{position:absolute;left:0;top:0;width:1200px;height:480px;background:linear-gradient(180deg,#f4f4f4,#e4e4e4)}
.hero-photo{position:absolute;left:0;top:0;width:1200px;height:480px;background:linear-gradient(100deg,rgba(255,255,255,.2) 0%,rgba(150,150,150,.35) 45%,rgba(210,210,210,.3) 100%)}
.hero-title{position:absolute;left:44px;top:150px;font:900 66px/1 "Roboto",sans-serif;color:var(--red);letter-spacing:-1px}
.hero-title span{display:block;color:var(--ink);font-weight:400;font-size:62px;margin-top:6px}
.hero-slide{position:absolute;left:600px;top:50px;width:540px;height:304px;background:var(--red);box-shadow:0 6px 20px rgba(0,0,0,.25);overflow:hidden}
.hero-slide .band{position:absolute;left:0;right:0;bottom:0;height:56px;background:var(--white)}
.hero-slide h2{position:absolute;left:40px;top:100px;font:700 30px "Roboto Condensed",sans-serif;color:var(--white);letter-spacing:.5px}
.hero-slide p{position:absolute;left:40px;top:142px;font-size:13px;color:#ffd3d7}
.hero-slide .brand{position:absolute;right:36px;bottom:18px}

/* brand stand-in */
.brand{display:flex;align-items:center;gap:5px;font:700 11px "Roboto",sans-serif;color:var(--red)}
.brand i{display:block;width:10px;height:10px;border-radius:50%;background:var(--red)}
.brand.light{color:var(--white)}
.brand.light i{background:var(--white)}

/* deck grid */
.deck{position:absolute;left:14px;top:500px;display:grid;grid-template-columns:repeat(3,380px);grid-auto-rows:214px;gap:14px 16px}
.slide{position:relative;background:var(--white);overflow:hidden;box-shadow:0 1px 4px rgba(0,0,0,.18)}
.slide .mark{position:absolute;left:0;bottom:10px;width:5px;height:5px;background:var(--red)}
.slide .foot{position:absolute;left:14px;right:14px;bottom:6px;display:flex;justify-content:space-between;font-size:4.5px;color:#aaa;border-top:.5px solid #e2e2e2;padding-top:2px}
.h{position:absolute;left:16px;top:14px;font:700 12px "Roboto Condensed",sans-serif;color:var(--ink)}
.h.red{color:var(--red)}
.p{font-size:6px;line-height:1.5;color:var(--gray)}
.abs{position:absolute}
.photo{position:absolute}
.photo.red{background:linear-gradient(135deg,#c7101f,#6a0a12)}
.photo.gray{background:linear-gradient(135deg,#b9b9b9,#6d6d6d)}
.photo.warm{background:linear-gradient(135deg,#8e5a4a,#3a2a2a)}
.photo.blue{background:linear-gradient(135deg,#b9d3e6,#6e93b3)}
.photo.soft{background:linear-gradient(135deg,#e9e9e9,#c9c9c9)}
.redbox{position:absolute;background:var(--red);color:var(--white)}
.pill{position:absolute;height:14px;background:var(--red);border-radius:7px;color:var(--white);font-size:6px;line-height:14px;padding-left:18px}
.icon{display:inline-block;width:9px;height:9px;background:var(--red);vertical-align:middle}
table{border-collapse:collapse;width:100%}
td,th{font-size:5.5px;padding:2.5px 4px;text-align:left;border-bottom:.5px solid #e2e2e2;color:var(--gray)}
th{background:var(--red);color:var(--white);font-weight:700}
.big{font:700 22px "Roboto Condensed",sans-serif;color:var(--red)}
</style>
</head>
<body>
<div class="canvas">

  <header class="hero">
    <div class="hero-photo" role="img" aria-label="Faded photo of a cheering crowd at a gaming event"></div>
    <h1 class="hero-title">Presentation<span>Deck</span></h1>
    <div class="hero-slide">
      <h2>PRESENTATION TITLE</h2>
      <p>Sub title here</p>
      <div class="band"></div>
      <div class="brand"><i></i>Meridian Gaming</div>
    </div>
  </header>

  <main class="deck">

    <!-- 1 title red -->
    <section class="slide">
      <div class="photo red" style="left:0;top:0;width:380px;height:140px" role="img" aria-label="Red-toned photo of dice on a gaming table"></div>
      <div class="abs" style="left:130px;top:60px;color:#fff;font:700 15px 'Roboto Condensed',sans-serif">Presentation Title Goes Here</div>
      <div class="abs" style="left:130px;top:80px;color:#ffd3d7;font-size:7px">Sub title here</div>
      <div class="brand abs" style="left:150px;top:165px"><i></i>Meridian Gaming</div>
    </section>

    <!-- 2 title band -->
    <section class="slide">
      <div class="photo blue" style="left:0;top:0;width:380px;height:110px" role="img" aria-label="Blue-toned photo of gaming chips and cards"></div>
      <div class="redbox" style="left:0;top:80px;width:380px;height:48px">
        <div class="abs" style="left:120px;top:10px;font:700 15px 'Roboto Condensed',sans-serif">Presentation Title</div>
        <div class="abs" style="left:120px;top:30px;font-size:7px;color:#ffd3d7">Sub title here</div>
      </div>
      <div class="brand abs" style="left:150px;top:160px"><i></i>Meridian Gaming</div>
    </section>

    <!-- 3 quote -->
    <section class="slide">
      <div class="photo soft" style="left:0;top:0;width:380px;height:214px" role="img" aria-label="Light gray photo of a casino interior"></div>
      <div class="redbox" style="left:150px;top:70px;width:170px;height:40px;font:700 11px/40px 'Roboto Condensed',sans-serif;text-align:center">Here add a short quote</div>
      <span class="mark"></span>
    </section>

    <!-- 4 simple text -->
    <section class="slide">
      <div class="h">Simple Text</div>
      <div class="abs p" style="left:16px;top:38px;width:348px">
        <p>Our venues welcome guests from many countries every year. We build fair, safe and modern gaming experiences for partners and investors.</p><br>
        <p>Our venues welcome guests from many countries every year. We build fair, safe and modern gaming experiences for partners and investors.</p><br>
        <p>Our venues welcome guests from many countries every year. We build fair, safe and modern gaming experiences for partners and investors.</p>
      </div>
      <div class="foot"><span>Confidential</span><span>04</span></div>
    </section>

    <!-- 5 two columns -->
    <section class="slide">
      <div class="h">Two Columns Text</div>
      <div class="abs" style="left:16px;top:40px;width:160px;height:40px;background:var(--gray-bg)"></div>
      <div class="abs p" style="left:16px;top:88px;width:160px">Our venues welcome guests from many countries every year. We build fair, safe and modern gaming experiences for partners and investors.</div>
      <div class="pill" style="left:200px;top:50px;width:160px">Add your key point</div>
      <div class="pill" style="left:200px;top:80px;width:160px">Add your key point</div>
      <div class="pill" style="left:200px;top:110px;width:160px">Add your key point</div>
      <div class="foot"><span>Confidential</span><span>05</span></div>
    </section>

    <!-- 6 text picture quote -->
    <section class="slide">
      <div class="h">Text, Picture and a Quote</div>
      <div class="abs p" style="left:16px;top:40px;width:90px">Our venues welcome guests from many countries every year. We build fair, safe and modern gaming experiences for partners and investors.</div>
      <div class="abs p" style="left:115px;top:40px;width:90px">Our venues welcome guests from many countries every year. We build fair, safe and modern gaming experiences for partners and investors.</div>
      <div class="photo red" style="left:220px;top:30px;width:145px;height:160px" role="img" aria-label="Photo of a playing card on a red background"></div>
      <div class="foot"><span>Confidential</span><span>06</span></div>
    </section>

    <!-- 7 photo with box -->
    <section class="slide">
      <div class="photo warm" style="left:0;top:0;width:380px;height:214px" role="img" aria-label="Photo of guests celebrating in a casino"></div>
      <div class="abs" style="left:16px;top:20px;width:130px;height:120px;background:#fff;padding:10px">
        <div style="height:3px;width:30px;background:var(--red);margin-bottom:6px"></div>
        <div class="p">Our venues welcome guests from many countries every year. We build fair, safe and modern gaming experiences for partners and investors.</div>
      </div>
    </section>

    <!-- 8 group -->
    <section class="slide">
      <div class="h">GROUP</div>
      <div class="abs" style="left:16px;top:40px;width:165px">
        <p class="p" style="margin-bottom:10px"><span class="icon"></span> <b>Company name</b> Short description line</p>
        <p class="p" style="margin-bottom:10px"><span class="icon"></span> <b>Company name</b> Short description line</p>
        <p class="p"><span class="icon"></span> <b>Company name</b> Short description line</p>
      </div>
      <div class="abs" style="left:200px;top:40px;width:165px">
        <p class="p" style="margin-bottom:10px"><span class="icon"></span> <b>Company name</b> Short description line</p>
        <p class="p" style="margin-bottom:10px"><span class="icon"></span> <b>Company name</b> Short description line</p>
        <p class="p"><span class="icon"></span> <b>Company name</b> Short description line</p>
      </div>
      <div class="foot"><span>Confidential</span><span>08</span></div>
    </section>

    <!-- 9 projects -->
    <section class="slide">
      <div class="h">Projects</div>
      <div class="abs" style="left:16px;top:40px;display:grid;grid-template-columns:repeat(2,168px);gap:12px">
        <div style="border-top:3px solid var(--red);padding-top:5px"><p class="p"><b>Project name</b><br>Short summary of the idea</p></div>
        <div style="border-top:3px solid var(--red);padding-top:5px"><p class="p"><b>Project name</b><br>Short summary of the idea</p></div>
        <div style="border-top:3px solid var(--red);padding-top:5px"><p class="p"><b>Project name</b><br>Short summary of the idea</p></div>
        <div style="border-top:3px solid var(--red);padding-top:5px"><p class="p"><b>Project name</b><br>Short summary of the idea</p></div>
      </div>
      <div class="redbox" style="left:16px;top:150px;width:348px;height:30px"></div>
      <div class="foot"><span>Confidential</span><span>09</span></div>
    </section>

    <!-- 10 text and two pictures -->
    <section class="slide">
      <div class="h">Text and Two Pictures</div>
      <div class="abs p" style="left:16px;top:40px;width:150px">Our venues welcome guests from many countries every year. We build fair, safe and modern gaming experiences for partners and investors.</div>
      <div class="photo gray" style="left:190px;top:35px;width:175px;height:70px" role="img" aria-label="Photo of a gaming hall"></div>
      <div class="photo red" style="left:190px;top:112px;width:175px;height:80px" role="img" aria-label="Photo of roulette wheel in red light"></div>
      <div class="foot"><span>Confidential</span><span>10</span></div>
    </section>

    <!-- 11 group photos -->
    <section class="slide">
      <div class="h">THE MERIDIAN GAMING GROUP</div>
      <div class="abs" style="left:16px;top:40px;display:grid;grid-template-columns:repeat(4,81px);gap:8px">
        <div><div class="photo red" style="position:relative;height:80px" role="img" aria-label="Photo of a venue"></div><div class="redbox" style="position:relative;height:16px;font-size:6px;line-height:16px;padding-left:5px">Venue One</div></div>
        <div><div class="photo warm" style="position:relative;height:80px" role="img" aria-label="Photo of a venue"></div><div class="redbox" style="position:relative;height:16px;font-size:6px;line-height:16px;padding-left:5px">Venue Two</div></div>
        <div><div class="photo gray" style="position:relative;height:80px" role="img" aria-label="Photo of a venue"></div><div class="redbox" style="position:relative;height:16px;font-size:6px;line-height:16px;padding-left:5px">Venue Three</div></div>
        <div><div class="photo red" style="position:relative;height:80px" role="img" aria-label="Photo of a venue"></div><div class="redbox" style="position:relative;height:16px;font-size:6px;line-height:16px;padding-left:5px">Venue Four</div></div>
      </div>
      <div class="foot"><span>Confidential</span><span>11</span></div>
    </section>

    <!-- 12 infographic -->
    <section class="slide">
      <div class="h">Infographic</div>
      <svg class="abs" style="left:150px;top:50px" width="80" height="80" viewBox="0 0 80 80">
        <circle cx="40" cy="40" r="30" fill="none" stroke="#e3051b" stroke-width="14" stroke-dasharray="44 3.1"/>
        <circle cx="40" cy="40" r="14" fill="#bdbdbd"/>
      </svg>
      <p class="abs p" style="left:20px;top:50px;width:110px;text-align:right"><b>Step title</b><br>Short note here</p>
      <p class="abs p" style="left:20px;top:105px;width:110px;text-align:right"><b>Step title</b><br>Short note here</p>
      <p class="abs p" style="left:250px;top:50px;width:110px"><b>Step title</b><br>Short note here</p>
      <p class="abs p" style="left:250px;top:105px;width:110px"><b>Step title</b><br>Short note here</p>
      <div class="foot"><span>Confidential</span><span>12</span></div>
    </section>

    <!-- 13 awesome arrows -->
    <section class="slide">
      <div class="abs" style="left:16px;top:18px;font:700 14px 'Roboto Condensed',sans-serif">Your <span style="color:var(--red)">Awesome</span> text here</div>
      <svg class="abs" style="left:24px;top:70px" width="150" height="60" viewBox="0 0 150 60">
        <polygon points="0,30 30,5 30,18 70,18 70,42 30,42 30,55" fill="#bdbdbd"/>
        <polygon points="150,30 120,5 120,18 80,18 80,42 120,42 120,55" fill="#e3051b"/>
      </svg>
      <div class="abs p" style="left:200px;top:70px;width:160px">Our venues welcome guests from many countries every year. We build fair, safe and modern gaming experiences for partners and investors.</div>
      <div class="foot"><span>Confidential</span><span>13</span></div>
    </section>

    <!-- 14 56% -->
    <section class="slide">
      <div class="abs" style="left:16px;top:18px;width:150px;font:700 11px/1.2 'Roboto Condensed',sans-serif">Here add some short text <span style="color:var(--red)">to explain some things</span></div>
      <div class="abs big" style="left:16px;top:80px">56%</div>
      <div class="abs p" style="left:16px;top:112px;width:150px">Our venues welcome guests from many countries every year. We build fair, safe and modern gaming experiences for partners and investors.</div>
      <div class="photo soft" style="left:200px;top:0;width:180px;height:214px" role="img" aria-label="Light photo of a gaming table"></div>
    </section>

    <!-- 15 numbers -->
    <section class="slide">
      <div class="abs" style="left:16px;top:18px;font:700 14px 'Roboto Condensed',sans-serif">Your <span style="color:var(--red)">Awesome</span> text here</div>
      <div class="abs" style="left:16px;top:90px;display:flex;gap:40px">
        <div><div class="big">98</div><p class="p">Venues worldwide</p></div>
        <div><div class="big">2021</div><p class="p">Founding year</p></div>
        <div><div class="big">150+</div><p class="p">Partner companies</p></div>
      </div>
      <div class="foot"><span>Confidential</span><span>15</span></div>
    </section>

    <!-- 16 chart -->
    <section class="slide">
      <div class="h">Chart</div>
      <svg class="abs" style="left:16px;top:45px" width="180" height="140" viewBox="0 0 180 140">
        <line x1="0" y1="130" x2="180" y2="130" stroke="#ccc"/>
        <rect x="10" y="40" width="12" height="90" fill="#e3051b"/><rect x="24" y="70" width="12" height="60" fill="#bdbdbd"/>
        <rect x="55" y="20" width="12" height="110" fill="#e3051b"/><rect x="69" y="60" width="12" height="70" fill="#bdbdbd"/>
        <rect x="100" y="55" width="12" height="75" fill="#e3051b"/><rect x="114" y="35" width="12" height="95" fill="#bdbdbd"/>
        <rect x="145" y="30" width="12" height="100" fill="#e3051b"/><rect x="159" y="80" width="12" height="50" fill="#bdbdbd"/>
      </svg>
      <div class="abs big" style="left:220px;top:50px">35 %</div>
      <div class="abs p" style="left:220px;top:82px;width:145px">Our venues welcome guests from many countries every year. We build fair, safe and modern gaming experiences for partners and investors.</div>
      <div class="foot"><span>Confidential</span><span>16</span></div>
    </section>

    <!-- 17 statistic -->
    <section class="slide">
      <div class="h">Statistic</div>
      <svg class="abs" style="left:30px;top:55px" width="320" height="90" viewBox="0 0 320 90">
        <circle cx="45" cy="45" r="36" fill="none" stroke="#e6e6e6" stroke-width="6"/>
        <circle cx="45" cy="45" r="36" fill="none" stroke="#e3051b" stroke-width="6" stroke-dasharray="113 226" transform="rotate(-90 45 45)"/>
        <text x="45" y="49" text-anchor="middle" font-family="Roboto,sans-serif" font-size="12" font-weight="700" fill="#222">50%</text>
        <circle cx="160" cy="45" r="40" fill="#e3051b"/>
        <text x="160" y="49" text-anchor="middle" font-family="Roboto,sans-serif" font-size="13" font-weight="700" fill="#fff">75%</text>
        <circle cx="275" cy="45" r="36" fill="none" stroke="#e6e6e6" stroke-width="6"/>
        <circle cx="275" cy="45" r="36" fill="none" stroke="#999" stroke-width="6" stroke-dasharray="181 226" transform="rotate(-90 275 45)"/>
        <text x="275" y="49" text-anchor="middle" font-family="Roboto,sans-serif" font-size="12" font-weight="700" fill="#222">80%</text>
      </svg>
      <p class="abs p" style="left:58px;top:155px">Add label</p>
      <p class="abs p" style="left:175px;top:155px">Add label</p>
      <p class="abs p" style="left:288px;top:155px">Add label</p>
      <div class="foot"><span>Confidential</span><span>17</span></div>
    </section>

    <!-- 18 table of content -->
    <section class="slide">
      <div class="h">Table Of Content</div>
      <div class="abs" style="left:130px;top:40px;width:235px">
        <table>
          <tr><th></th><th>Q1</th><th>Q2</th><th>Q3</th></tr>
          <tr><td>Text</td><td>Text</td><td>Text</td><td>Text</td></tr>
          <tr><td>Text</td><td>Text</td><td>Text</td><td>Text</td></tr>
          <tr><td>Text</td><td>Text</td><td>Text</td><td>Text</td></tr>
          <tr><td>Text</td><td>Text</td><td>Text</td><td>Text</td></tr>
          <tr><td>Text</td><td>Text</td><td>Text</td><td>Text</td></tr>
        </table>
      </div>
      <div class="foot"><span>Confidential</span><span>18</span></div>
    </section>

    <!-- 19 table of content wide -->
    <section class="slide">
      <div class="h">Table Of Content</div>
      <div class="abs" style="left:16px;top:40px;width:348px">
        <table>
          <tr><th>Item</th><th>2019</th><th>2020</th><th>2021</th><th>2022</th></tr>
          <tr><td>Text</td><td>Text</td><td>Text</td><td>Text</td><td>Text</td></tr>
          <tr><td>Text</td><td>Text</td><td>Text</td><td>Text</td><td>Text</td></tr>
          <tr><td>Text</td><td>Text</td><td>Text</td><td>Text</td><td>Text</td></tr>
          <tr><td>Text</td><td>Text</td><td>Text</td><td>Text</td><td>Text</td></tr>
          <tr><td>Text</td><td>Text</td><td>Text</td><td>Text</td><td>Text</td></tr>
          <tr><td>Text</td><td>Text</td><td>Text</td><td>Text</td><td>Text</td></tr>
        </table>
      </div>
      <div class="foot"><span>Confidential</span><span>19</span></div>
    </section>

    <!-- 20 executive board -->
    <section class="slide">
      <div class="h">Our Executive Board</div>
      <div class="abs" style="left:16px;top:40px;width:348px;height:150px;background:var(--gray-bg)"></div>
      <div class="photo gray" style="left:40px;top:55px;width:80px;height:90px" role="img" aria-label="Portrait of board member"></div>
      <p class="abs p" style="left:130px;top:120px"><b>Anna Berger</b><br>Chief Executive</p>
      <div class="photo gray" style="left:200px;top:55px;width:80px;height:90px" role="img" aria-label="Portrait of board member"></div>
      <p class="abs p" style="left:290px;top:120px"><b>Lukas Reiter</b><br>Chief Financial</p>
    </section>

    <!-- 21 international -->
    <section class="slide">
      <div class="h">MERIDIAN GAMING INTERNATIONAL</div>
      <div class="photo soft" style="left:30px;top:40px;width:320px;height:150px" role="img" aria-label="World map showing international locations"></div>
      <svg class="abs" style="left:30px;top:40px" width="320" height="150" viewBox="0 0 320 150">
        <circle cx="170" cy="50" r="4" fill="#e3051b"/><circle cx="90" cy="60" r="4" fill="#e3051b"/>
        <circle cx="240" cy="80" r="4" fill="#e3051b"/><circle cx="190" cy="100" r="4" fill="#e3051b"/>
      </svg>
    </section>

    <!-- 22 timeline -->
    <section class="slide">
      <div class="abs" style="left:16px;top:14px;font:700 12px 'Roboto Condensed',sans-serif">Your <span style="color:var(--red)">Company</span> Timeline</div>
      <div class="abs" style="left:60px;top:40px;width:3px;height:150px;background:var(--red)"></div>
      <div class="abs" style="left:16px;top:45px;display:grid;gap:18px">
        <p class="p"><b style="color:var(--red)">2018</b> &nbsp;&nbsp;&nbsp;&nbsp;&nbsp;&nbsp;&nbsp;&nbsp;Milestone text here</p>
        <p class="p"><b style="color:var(--red)">2019</b> &nbsp;&nbsp;&nbsp;&nbsp;&nbsp;&nbsp;&nbsp;&nbsp;Milestone text here</p>
        <p class="p"><b style="color:var(--red)">2020</b> &nbsp;&nbsp;&nbsp;&nbsp;&nbsp;&nbsp;&nbsp;&nbsp;Milestone text here</p>
        <p class="p"><b style="color:var(--red)">2021</b> &nbsp;&nbsp;&nbsp;&nbsp;&nbsp;&nbsp;&nbsp;&nbsp;Milestone text here</p>
      </div>
      <div class="redbox" style="left:200px;top:40px;width:160px;height:150px;background:var(--gray-bg)"></div>
      <div class="foot"><span>Confidential</span><span>22</span></div>
    </section>

    <!-- 23 page break -->
    <section class="slide" style="background:var(--red)">
      <div class="brand light abs" style="left:150px;top:80px"><i></i>Meridian Gaming</div>
      <div class="abs" style="left:0;right:0;top:110px;text-align:center;color:#fff;font:700 18px 'Roboto Condensed',sans-serif">Page break</div>
    </section>

    <!-- 24 thank you -->
    <section class="slide">
      <div class="photo soft" style="left:0;top:0;width:380px;height:214px" role="img" aria-label="Faded photo of a casino lounge"></div>
      <div class="redbox" style="left:90px;top:40px;width:90px;height:130px;background:#fff;box-shadow:0 1px 4px rgba(0,0,0,.2)">
        <div class="brand abs" style="left:8px;top:58px;font-size:8px"><i></i>Meridian</div>
      </div>
      <div class="abs" style="left:195px;top:95px;font:700 22px 'Roboto Condensed',sans-serif;color:#8a8a8a">THANK YOU</div>
    </section>

  </main>
</div>
</body>
</html>
```